Business Card Design and Basic Text Logo

We are looking for a business card design for an e-business company. Our business is the parent company of a few website businesses. The final logo and business card design will communicate a conservative but modern and expansive business

The Logo text is: 87Merchant
We would also like a basic text logo design for 87Merchant. The logo could also fill up the reverse side of the business card.

The colours we would like to use are:
White
Navy
Black

This is the text that will be added to the card:

Dean Colley
Business Development Manager

Phone: +61 417 658 294
Email: dean.colley@87merchant.com.au

Industry/Entity Type

Business

Logo Text

87Merchant

Logo styles of interest
Pictorial/Combination Logo
Requirements
Must have
• Modern and attractive design
Nice to have
• communicate a conservative but modern and expansive business
Should not have
• Should be too dull and plan
• But also should be overly colourful

```html
<!DOCTYPE html>
<html lang="en">
<head>
<meta charset="utf-8">
<title>87Merchant Business Card</title>
<link rel="stylesheet" href="https://fonts.googleapis.com/css2?family=Open+Sans:wght@300;400&display=swap">
<style>
  :root {
    --backdrop: #3a4648;
    --card-black: #0b0b0c;
    --navy: #0f2d52;
    --navy-text: #2c4f7c;
    --white: #f2f2f2;
    --muted: #c9ccd0;
  }
  * { margin: 0; padding: 0; box-sizing: border-box; }
  html, body { width: 1200px; height: 1000px; overflow: hidden; }
  body {
    background: var(--backdrop);
    font-family: "Open Sans", Arial, sans-serif;
    position: relative;
  }
  .card {
    position: absolute;
    width: 525px;
    height: 300px;
    background: var(--card-black);
    overflow: hidden;
    box-shadow: 0 6px 18px rgba(0,0,0,0.45);
  }
  .card-front { left: 90px; top: 140px; }
  .card-back { left: 585px; top: 560px; }

  .band {
    position: absolute;
    left: 0;
    width: 100%;
    background: var(--navy);
  }
  .card-front .band { top: 196px; height: 46px; }
  .card-back .band { top: 46px; height: 40px; }

  .brand {
    font-weight: 300;
    letter-spacing: 1px;
    white-space: nowrap;
  }
  .card-front .brand {
    position: absolute;
    left: 34px;
    top: 26px;
    font-size: 38px;
    color: var(--white);
  }
  .holder {
    position: absolute;
    left: 36px;
    top: 90px;
  }
  .holder-name {
    font-size: 19px;
    font-weight: 400;
    color: var(--white);
  }
  .holder-title {
    font-size: 11px;
    color: var(--navy-text);
    margin-top: 2px;
  }
  .contacts {
    position: absolute;
    left: 36px;
    top: 142px;
    list-style: none;
  }
  .contacts li {
    display: flex;
    align-items: center;
    gap: 8px;
    font-size: 11px;
    color: var(--muted);
    height: 17px;
  }
  .contacts svg { width: 12px; height: 12px; flex: none; }

  .card-back .brand {
    position: absolute;
    left: 0;
    right: 0;
    top: 140px;
    text-align: center;
    font-size: 52px;
    color: var(--white);
  }
</style>
</head>
<body>

<section class="card card-front" aria-label="Business card front">
  <div class="band"></div>
  <div class="brand">87Merchant</div>
  <div class="holder">
    <div class="holder-name">Dean Colley</div>
    <div class="holder-title">Business Development Manager</div>
  </div>
  <ul class="contacts">
    <li>
      <svg viewBox="0 0 12 12" aria-hidden="true"><circle cx="6" cy="6" r="6" fill="#d8d8d8"/><path d="M4 3.2 l1.2 1.4 -0.6 0.7 a4 4 0 0 0 2.1 2.1 l0.7-0.6 1.4 1.2 -0.8 0.9 C5.6 8.6 3.4 6.4 3.1 4 Z" fill="#0b0b0c"/></svg>
      <span>+61 417 658 294</span>
    </li>
    <li>
      <svg viewBox="0 0 12 12" aria-hidden="true"><rect x="0.5" y="2" width="11" height="8" fill="#d8d8d8"/><path d="M0.5 2 L6 6.5 L11.5 2" fill="none" stroke="#0b0b0c" stroke-width="1"/></svg>
      <span>dean.colley@87merchant.com.au</span>
    </li>
    <li>
      <svg viewBox="0 0 12 12" aria-hidden="true"><circle cx="6" cy="6" r="5.5" fill="#d8d8d8"/><ellipse cx="6" cy="6" rx="2.3" ry="5.5" fill="none" stroke="#0b0b0c" stroke-width="0.8"/><line x1="0.5" y1="6" x2="11.5" y2="6" stroke="#0b0b0c" stroke-width="0.8"/></svg>
      <span>www.87merchant.com.au</span>
    </li>
  </ul>
</section>

<section class="card card-back" aria-label="Business card back">
  <div class="band"></div>
  <div class="brand">87Merchant</div>
</section>

</body>
</html>
```